Business card for our large format printing and installation business

We want a professional looking business card for our business. We manufacture and install Signs.

On the back of the card add this info
Large Format Graphics Printing & Installations, Event Graphics, Banners, Posters, Vehicle Fleet Graphics, Boat Wraps, Wall Murals, Decals,Displays,Signs,Plaques,Digital Signs

On the Front of the card add the Tallmoor Signs logo, plus On the back of the card add the Orange Tallmoor Wraps logo. The 2 vector logos are attached to the design brief.

Target Market(s)

Local business owners

Contact Information for Business Card

Colors
f37122
f68d4e
f9ba93

Requirements
Must have
• On the Front of the card add the Tallmoor Signs logo, plus On the back of the card add the Orange Tallmoor Wraps logo. The 2 vector logos are attached to the design brief.

```html
<!DOCTYPE html>
<html lang="en">
<head>
<meta charset="utf-8">
<title>Tallmoor Signs – Business Card</title>
<link href="https://fonts.googleapis.com/css2?family=Open+Sans:wght@400;600;700;800&display=swap" rel="stylesheet">
<style>
  :root {
    --page-bg: #dcdcdc;
    --card-bg: #1f1d1d;
    --gold-light: #f7d31b;
    --gold-mid: #f5a91d;
    --orange: #f37122;
    --orange-soft: #f68d4e;
    --text-light: #e9e6e3;
  }
  * { margin: 0; padding: 0; box-sizing: border-box; }
  html, body {
    width: 1200px; height: 787px; overflow: hidden;
    background: var(--page-bg);
    font-family: "Open Sans", Arial, sans-serif;
  }
  .sheet {
    width: 1200px; height: 787px;
    display: flex; align-items: center; justify-content: center; gap: 40px;
  }
  .card {
    position: relative;
    width: 540px; height: 309px;
    background: var(--card-bg);
    box-shadow: 0 6px 18px rgba(0,0,0,.25);
    overflow: hidden;
    color: var(--text-light);
  }
  .gold-band {
    position: absolute; left: 0; right: 0; bottom: 0; height: 16px;
    background: linear-gradient(90deg, var(--gold-light), var(--gold-mid) 35%, var(--orange) 55%, var(--gold-light) 80%, var(--gold-mid));
  }
  .hairline {
    position: absolute; height: 1px;
    background: linear-gradient(90deg, var(--gold-mid), var(--gold-light));
  }
  .wordmark {
    position: absolute;
    font-weight: 800;
    color: var(--orange);
    line-height: 0.95;
    text-align: right;
    letter-spacing: -0.5px;
  }

  /* Front */
  .front .holder { position: absolute; left: 34px; top: 30px; }
  .front .holder-name { font-size: 17px; font-weight: 700; color: var(--gold-mid); letter-spacing: .3px; }
  .front .holder-role { font-size: 12px; margin-top: 2px; }
  .front .line-top { left: 34px; top: 84px; width: 460px; }
  .front .contact { position: absolute; left: 34px; top: 98px; list-style: none; font-size: 12.5px; }
  .front .contact li { display: flex; align-items: center; gap: 8px; height: 19px; }
  .front .contact svg { width: 11px; height: 11px; fill: var(--gold-mid); }
  .front .wordmark { right: 40px; top: 110px; font-size: 44px; }
  .front .address { position: absolute; right: 40px; bottom: 34px; text-align: right; font-size: 13px; line-height: 1.4; }

  /* Back */
  .back .line-top { left: 34px; top: 40px; width: 470px; }
  .back .services { position: absolute; left: 34px; top: 54px; font-size: 12.5px; line-height: 1.55; }
  .back .line-bottom { left: 34px; top: 142px; width: 470px; }
  .back .wordmark { right: 40px; top: 170px; font-size: 40px; }
</style>
</head>
<body>
<main class="sheet">

  <section class="card front" aria-label="Business card front">
    <div class="holder">
      <div class="holder-name">DORIAN HALVERS</div>
      <div class="holder-role">Owner</div>
    </div>
    <div class="hairline line-top"></div>
    <ul class="contact">
      <li><svg viewBox="0 0 24 24" aria-hidden="true"><path d="M6.6 10.8a15.1 15.1 0 0 0 6.6 6.6l2.2-2.2c.3-.3.7-.4 1-.2 1.1.4 2.3.6 3.6.6.6 0 1 .4 1 1V20c0 .6-.4 1-1 1A17 17 0 0 1 3 4c0-.6.4-1 1-1h3.5c.6 0 1 .4 1 1 0 1.3.2 2.5.6 3.6.1.3 0 .7-.2 1z"/></svg>000.123.456.789</li>
      <li><svg viewBox="0 0 24 24" aria-hidden="true"><path d="M6 2h9l3 3v4H6zM4 10h16a2 2 0 0 1 2 2v6h-4v4H6v-4H2v-6a2 2 0 0 1 2-2zm4 6v4h8v-4z"/></svg>000.123.456.789</li>
      <li><svg viewBox="0 0 24 24" aria-hidden="true"><path d="M2 5h20v14H2zm2 2v.5l8 5.5 8-5.5V7z"/></svg>info@yourwebsitename.com</li>
      <li><svg viewBox="0 0 24 24" aria-hidden="true"><path d="M12 2a10 10 0 1 0 0 20 10 10 0 0 0 0-20zm6.9 9h-3a15 15 0 0 0-1.3-6A8 8 0 0 1 18.9 11zM12 4.1c.9 1.2 1.7 3.7 1.9 6.9h-3.8c.2-3.2 1-5.7 1.9-6.9zM9.4 5a15 15 0 0 0-1.3 6h-3A8 8 0 0 1 9.4 5zm-4.3 8h3a15 15 0 0 0 1.3 6 8 8 0 0 1-4.3-6zm6.9 6.9c-.9-1.2-1.7-3.7-1.9-6.9h3.8c-.2 3.2-1 5.7-1.9 6.9zm2.6-.9a15 15 0 0 0 1.3-6h3a8 8 0 0 1-4.3 6z"/></svg>www.yourwebsitename.com</li>
    </ul>
    <div class="wordmark">Tallmoor<br>Signs</div>
    <address class="address" style="font-style:normal">2180 Fenwick Ave<br>Suite 40<br>Larchmont Hills, MD 21390</address>
    <div class="gold-band"></div>
  </section>

  <section class="card back" aria-label="Business card back">
    <div class="hairline line-top"></div>
    <p class="services">
      Large Format Graphics Printing &amp; Installations<br>
      Event Graphics, Banners, Posters<br>
      Vehicle Fleet Graphics, Boat Wraps, Wall Murals, Decals<br>
      Displays, Signs, Plaques, Digital Signs
    </p>
    <div class="hairline line-bottom"></div>
    <div class="wordmark">Tallmoor<br>Wraps</div>
    <div class="gold-band"></div>
  </section>

</main>
</body>
</html>
```